依頼詳細
・依頼内容: チラシデータ作成
・使用用途: チラシ(チラシの内容をHPにも掲載したいと考えております)
・サイズ: 折りチラシ / 外3つ折り / A4の1/3仕上がり
※完成したものをOPP封筒に入れます(当方で)。
表紙には店名や訴求文言などが見えるデザインにして下さい。
・デザイン要望: 既存の治療法ではないことから、「差別化」をコンセプトに、店舗イメージも既存の整体院・整骨院風ではなく、サロン風なオシャレなデザインにしております。
ただ、悩みどころなのですが、イラストのイメージはオシャレやクールなものにすると患者様に来て頂きにくいので分かりやすく、馴染みやすい、読んでももらいやすい(見てもらいやすい)ものにした方が良いのかと思っております。
・ターゲットカスタマー: 30歳代後半以降の方(もちろん若い方もウェルカム)※価格が少し高額な為、年齢層を上げています。
・男女比: 男性4:女性6
・ターゲット特徴
「芦屋」という高級な土地柄もあってか?初めてのものには飛びつかれず、財布の紐は固いが、良いものや価値があるものにはお金を出し渋らない特徴があるようです。

その他、不明な点があればご連絡下さい。

P.S.
この療法は自ら良いと思い、大手企業を脱サラし開院しました。
このチャレンジが成功するよう、お力添え頂けましたら幸いです。

宜しくお願い致します。
記載項目
院名: 葉月MELLOWY
詳細は下記HPをご覧下さい。
https://www.hazuki-mellowy.example/
サイズ
A4
ページ数
両面
希望イメージ
シンプル 複雑
単色 カラフル
暗い 明るい
日常 高級
遊び心 厳粛
未来的 伝統的
女性的 男性的
希望する色
緑系、水色系、無彩色系
納品ファイル
• 高解像度JPG (.jpg)
• イラストレーター形式 (.ai)
• PNG形式 (.png)
補足説明
現在、当方で自作したチラシを添付致します。(プリモアで印刷する際に印刷範囲などの若干の修正が入りました)
イラストなどで図説したかったのですが、スキルが無いため諦めました。
登録した内容に現チラシのファイルが添付されていなかった可能性があるので再度添付致します。
補足説明させて頂きます。

当院では、筋肉や関節にできてしまった「しこり」を専門器具(ローリング器)を使って見つけ、取り除いていきます。
・「しこり」とは?
体中にできる固くなった組織です。
肩こりのコリのような見つけやすいものから体の奥深くの筋肉や関節にできる、日々のケアでは回復しにくいものです。
・「しこり」ができる原因は?
・内臓疲労、精神的ストレス、姿勢の悪さ、怪我の後遺症などです。
・「しこり」ができると
痛みが発生します。そして、血流やリンパの流れが滞り様々な不調を引き起こします。
例えば、頭痛、腰痛、肩こり、眼精疲労、体の歪み、むくみ、冷え性、内臓の疲れなど。
「しこり」は骨を守る筋肉につき、しこりが無くなると歪んでしまった体(骨)も正常な位置に戻ります。

⇒従って、「しこり」を取り除くことが重要です。
ローリング療法なら、点で押さえる手のマッサージや針で刺す鍼灸などとは「違い」、ローリング器で全身を転がしていくことにより「体の奥のしこりまで逃さず取り除いていくことが出来きます」。
さらに、内臓の働きを良くし、自然治癒力を高める効果も期待できます。

イラストのイメージですが、
・「しこり」が筋肉や関節に癒着している様子。また、それにより血流やリンパの流れが滞っている様子。
・「しこり」が筋肉にでき体が歪んでしまい、取り除くと姿勢が正常になる様子
・ローリング器で「しこり」を押しつぶし、なだらかにしている様子

他に良さを伝えるのに良いイラストがあればご提案下さい。

また、ローリング協会HPもご参照下さい。https://www.suwaren-kai.example/index.htm
■ 選んだ理由

ローリング療法の概要を興味のない方に対し、「いかに目を向けてもらい、読んでもらい、理解して頂くか」ということに重点を置きました。
その点から、いかにフレンドリーで興味を持ってもらえるイラストであるかという点から選ばせて頂きました。
(当院コンセプトイメージとの両立で悩みましたが、チラシは読んで頂いてなんぼなので、興味を持って頂いてなんぼなので、その点は妥協する点もありました)

■ 提案者全員のお礼・コメント

この度はお忙しい中、短納期で素晴らしい案をご提案いただき誠に有難う御座いました。

小生の大まかな依頼にも関わらず、施術内容を調べ、正しくご理解いただきイラストで表して頂きました。
(皆様、技術に対する理解能力が高く、また全体のトーン&マナーも当院のコンセプトをよくご理解頂いており正直驚いたの一言です。

残念ながら、この度はお仕事をお願いすることが出来ませんでしたが、また別の機会があれば是非ご協力頂きましたら幸甚です。

改めて有難う御座いました。

```html
<!DOCTYPE html>
<html lang="ja">
<head>
<meta charset="utf-8">
<title>葉月MELLOWY ボディメンテナンススタジオ</title>
<link rel="stylesheet" href="https://fonts.googleapis.com/css2?family=Noto+Sans+JP:wght@400;500;700;900&family=Montserrat:wght@800&family=Cormorant+Garamond:ital,wght@1,500&display=swap">
<style>
  :root {
    --brand-blue: #1d9ee2;
    --ink: #111111;
    --white: #ffffff;
    --accent-yellow: #ffe94a;
    --photo-top: #d9d4cf;
    --photo-bottom: #7b7775;
  }
  html, body {
    margin: 0;
    padding: 0;
    width: 1200px;
    height: 2512px;
    overflow: hidden;
    background: var(--brand-blue);
  }
  .flyer-cover {
    position: relative;
    width: 1200px;
    height: 2512px;
    background: var(--brand-blue);
    font-family: "Noto Sans JP", sans-serif;
    color: var(--white);
  }
  .brand-badge {
    position: absolute;
    left: 460px;
    top: 0;
    width: 280px;
    height: 280px;
    background: var(--ink);
    display: flex;
    align-items: center;
    justify-content: center;
  }
  .brand-badge__name {
    font-family: "Noto Sans JP", sans-serif;
    font-weight: 500;
    font-size: 30px;
    letter-spacing: 1px;
    color: var(--white);
  }
  .studio-type {
    position: absolute;
    top: 580px;
    width: 100%;
    text-align: center;
    font-size: 52px;
    font-weight: 500;
    letter-spacing: 2px;
    margin: 0;
  }
  .studio-name {
    position: absolute;
    top: 660px;
    width: 100%;
    text-align: center;
    font-family: "Montserrat", sans-serif;
    font-weight: 800;
    font-size: 160px;
    line-height: 1;
    letter-spacing: 4px;
    margin: 0;
  }
  .treatment-photo {
    position: absolute;
    left: 0;
    top: 930px;
    width: 1200px;
    height: 730px;
    box-sizing: border-box;
    border-top: 20px solid var(--ink);
    border-bottom: 20px solid var(--ink);
    background: linear-gradient(180deg, var(--photo-top) 0%, #bdb7b2 55%, var(--photo-bottom) 100%);
  }
  .tagline {
    position: absolute;
    top: 1810px;
    width: 100%;
    text-align: center;
    font-size: 44px;
    font-weight: 500;
    margin: 0;
  }
  .motto {
    position: absolute;
    left: 0;
    top: 1990px;
    width: 1200px;
    height: 240px;
  }
  .motto text {
    font-family: "Cormorant Garamond", serif;
    font-style: italic;
    font-weight: 500;
    font-size: 66px;
    fill: var(--white);
  }
  .worries {
    position: absolute;
    top: 2232px;
    width: 100%;
    text-align: center;
    font-size: 34px;
    line-height: 50px;
    color: var(--ink);
    margin: 0;
  }
  .invitation {
    position: absolute;
    top: 2385px;
    width: 100%;
    text-align: center;
    font-size: 54px;
    font-weight: 700;
    margin: 0;
  }
  .invitation__method {
    color: var(--accent-yellow);
  }
</style>
</head>
<body>
  <main class="flyer-cover">
    <div class="brand-badge">
      <span class="brand-badge__name">葉月MELLOWY</span>
    </div>

    <p class="studio-type">葉月 ボディメンテナンススタジオ</p>
    <h1 class="studio-name">MELLOWY</h1>

    <div class="treatment-photo" role="img" aria-label="施術者がローリング器で、うつ伏せに寝た女性の背中をほぐしている写真"></div>

    <p class="tagline">手では見つけにくいコリにアプローチします</p>

    <svg class="motto" viewBox="0 0 1200 240" aria-label="Make you Healthy and Beautiful">
      <defs>
        <path id="motto-arc" d="M140 110 Q600 250 1080 190"/>
      </defs>
      <text><textPath href="#motto-arc" startOffset="50%" text-anchor="middle">Make you Healthy and Beautiful</textPath></text>
    </svg>

    <p class="worries">身体が凝った…　身体が痛い…<br>そんな時はマッサージ?それとも整体ですか?</p>

    <p class="invitation">一度、「<span class="invitation__method">ローリング療法</span>」を試してみませんか?</p>
  </main>
</body>
</html>
```